Need image design for a Facebook post promo

We need a Facebook suitable image for Facebook promotion showcasing the award winners of a book competition.

The awards took place at the Writers Page Premiere and Fair. we have six awards winners and we want to display the winning authors names and photos and book images on the design.

We want our logo (WPPF) and the logo of our major sponsor TRS Press to be prominent on the design.

I will attach the logos plus a sample flyer of our event to get a feel of the theme for the event. I will also attach the photo names of the winners.

Link for authors photos and books (6):

https://files.sharevault.example/folders/7pQ2xLm9RtY4vBn8KcW3zHj5DfG6sAe1?usp=sharing

Please display our website: pagefairnest.com.au

```html
<!DOCTYPE html>
<html lang="en">
<head>
<meta charset="utf-8">
<title>Book of the Year 2022 – Writers Page Premiere and Fair</title>
<link rel="stylesheet" href="https://fonts.googleapis.com/css2?family=Bebas+Neue&family=Libre+Baskerville:ital@0;1&family=Montserrat:wght@600;700;800&display=swap">
<style>
  :root{
    --navy:#0c2d4a;
    --crimson:#d1435b;
    --gold:#eaa93d;
    --teal:#23708c;
    --steel:#2b5573;
    --paper:#ffffff;
    --mist:#f1f1f3;
    --ink:#111111;
    --cover-gold:#e6b54a;
  }
  *{margin:0;padding:0;box-sizing:border-box}
  html,body{width:1200px;height:849px;overflow:hidden;background:var(--paper)}
  .board{position:relative;width:1200px;height:849px;background:var(--paper)}
  .poster{position:absolute;top:131px;width:419px;height:593px;border:9px solid var(--frame);background:var(--frame)}
  .poster--navy{left:137px;--frame:var(--navy)}
  .poster--gold{left:647px;--frame:var(--gold)}
  .poster__inner{position:absolute;inset:0;background:linear-gradient(160deg,#ffffff 0%,var(--mist) 45%,#ffffff 70%,var(--mist) 100%);overflow:hidden}

  .title{position:absolute;left:29px;top:14px;font-family:'Bebas Neue',sans-serif;line-height:.86;font-weight:400}
  .title__book{display:block;font-size:76px;color:var(--crimson);letter-spacing:-1px}
  .title__year{display:block;font-size:33px;color:var(--gold);letter-spacing:-.4px;margin-top:3px}
  .title__num{display:block;font-size:72px;color:var(--navy);letter-spacing:-1px;margin-top:2px;margin-left:4px}

  .event{position:absolute;left:206px;top:36px;width:176px;text-align:center;font-family:'Montserrat',sans-serif}
  .event__mark{display:block;font-weight:800;font-size:44px;color:var(--crimson);letter-spacing:1px;line-height:1}
  .event__name{display:block;margin-top:6px;font-weight:700;font-size:7.6px;color:var(--navy);letter-spacing:.2px;border-top:1.5px solid var(--navy);padding-top:4px}

  .winner{position:absolute;width:173px;height:101px;display:flex;box-shadow:0 2px 4px rgba(0,0,0,.18)}
  .winner__label{width:17px;height:100%;background:var(--band);display:flex;align-items:center;justify-content:center;overflow:hidden}
  .winner__label span{writing-mode:vertical-rl;transform:rotate(180deg);font-family:'Bebas Neue',sans-serif;font-size:9.6px;color:#fff;letter-spacing:.2px;white-space:nowrap}
  .winner__label--long span{font-size:8.4px;letter-spacing:0}
  .winner__photo{width:85px;height:100%}
  .col-a{left:22px}.col-b{left:206px}
  .row-1{top:179px}.row-2{top:295px}.row-3{top:412px}
  .band-gold{--band:var(--gold)}
  .band-crimson{--band:var(--crimson)}
  .band-teal{--band:var(--teal)}
  .band-steel{--band:var(--steel)}
  .band-navy{--band:var(--navy)}
  .photo-warm{background:linear-gradient(160deg,#a89b8c,#7d7265)}
  .photo-dark{background:linear-gradient(160deg,#4a4a4a,#1f1f22)}
  .photo-studio{background:linear-gradient(160deg,#e9e9ea,#bdbdc0)}
  .photo-window{background:linear-gradient(160deg,#c9d2d6,#2a3448)}

  .cover{position:relative;width:71px;height:100%;display:flex;flex-direction:column;align-items:center;justify-content:space-between;text-align:center;padding:4px 3px 3px;overflow:hidden;color:#fff}
  .cover__art{position:absolute;inset:0;z-index:0}
  .cover > *:not(.cover__art){position:relative;z-index:1}
  .cover__author{font-family:'Montserrat',sans-serif;font-weight:700;font-size:4.8px;letter-spacing:.4px;text-transform:uppercase;white-space:nowrap}
  .cover__title{font-family:'Bebas Neue',sans-serif;line-height:.9;white-space:nowrap}
  .cover__serif{font-family:'Libre Baskerville',serif;line-height:1.05}

  .cover-taupe .cover__art{background:linear-gradient(180deg,#9d9184,#6f8a3e)}
  .cover-taupe .cover__title{font-size:21px;color:var(--cover-gold);letter-spacing:.5px}

  .cover-orange .cover__art{background:linear-gradient(180deg,#f59a1b,#e27808)}
  .cover-orange .cover__serif{font-size:7.4px;color:#fff4e0;margin-top:26px}
  .cover-orange .cover__serif em{display:block;font-size:8.4px;color:#fff}
  .cover-orange .cover__author{color:#fff4e0;font-family:'Libre Baskerville',serif;font-weight:400;font-size:4.2px}

  .cover-navy .cover__art{background:linear-gradient(180deg,#1a3b5e,#0f2640)}
  .cover-navy .cover__title{font-size:12.5px;color:var(--cover-gold)}
  .cover-navy .cover__author{color:var(--cover-gold);font-size:5px}

  .cover-cyan{padding-bottom:0}
  .cover-cyan .cover__art{background:linear-gradient(180deg,#1aa8d0,#0f7fa6)}
  .cover-cyan .cover__title{font-size:15px;margin-top:16px;line-height:.85}
  .cover-cyan .cover__author{width:71px;margin:0 -3px;background:#2b2b2b;padding:2px 0;font-family:'Libre Baskerville',serif;font-weight:400;font-size:4.6px}

  .cover-charcoal .cover__art{background:linear-gradient(180deg,#3b362f,#8c7a45)}
  .cover-charcoal .cover__serif{font-size:9.4px;color:var(--cover-gold)}
  .cover-charcoal .cover__author{color:#f1e6cf;font-weight:600;font-size:4.6px;letter-spacing:.8px}

  .cover-sand{padding-bottom:0}
  .cover-sand .cover__art{background:linear-gradient(180deg,#d8c6ab,#7a2a3c)}
  .cover-sand .cover__serif{font-size:5.8px;font-style:italic;color:#3a2a22}
  .cover-sand .cover__author{width:71px;margin:0 -3px;background:#7a2a3c;padding:2px 0;font-family:'Libre Baskerville',serif;font-style:italic;font-weight:400;font-size:5.2px;text-transform:none;letter-spacing:0}

  .sponsor{position:absolute;right:12px;top:526px;display:flex;align-items:center;gap:4px;font-family:'Montserrat',sans-serif;font-weight:800;font-size:15px;color:var(--ink)}
  .sponsor__dot{width:9px;height:9px;background:var(--ink)}
  .footer{position:absolute;left:0;bottom:0;width:100%;height:36px}
  .footer svg{position:absolute;inset:0;width:100%;height:100%}
  .footer__url{position:absolute;left:0;right:0;bottom:4px;text-align:center;font-family:'Montserrat',sans-serif;font-weight:600;font-size:10.5px;color:#fff;letter-spacing:.2px}
</style>
</head>
<body>
<div class="board">

  <section class="poster poster--navy">
    <div class="poster__inner">
      <h1 class="title"><span class="title__book">BOOK</span><span class="title__year">OF THE YEAR</span><span class="title__num">2022</span></h1>
      <div class="event"><span class="event__mark">WPPF</span><span class="event__name">WRITERS PAGE PREMIERE AND FAIR</span></div>

      <div class="winner col-a row-1 band-gold">
        <div class="winner__label"><span>BOOK OF THE YEAR - GOLD</span></div>
        <div class="winner__photo photo-warm" role="img" aria-label="Portrait of author Maren Holloway"></div>
        <div class="cover cover-taupe"><div class="cover__art" role="img" aria-label="Cover artwork with the author seated"></div><p class="cover__author">Maren Holloway</p><p class="cover__title">TRADE</p></div>
      </div>
      <div class="winner col-b row-1 band-crimson">
        <div class="winner__label"><span>BOOK OF THE YEAR - SILVER</span></div>
        <div class="winner__photo photo-dark" role="img" aria-label="Portrait of author Delia Brennan"></div>
        <div class="cover cover-orange"><div class="cover__art" role="img" aria-label="Orange cover with a line drawing of open hands"></div><p class="cover__serif">the<em>Mindful</em>Steward</p><p class="cover__author">Delia Brennan</p></div>
      </div>
      <div class="winner col-a row-2 band-teal">
        <div class="winner__label"><span>BOOK OF THE YEAR - BRONZE</span></div>
        <div class="winner__photo photo-window" role="img" aria-label="Portrait of author Vikram Sethi"></div>
        <div class="cover cover-navy"><div class="cover__art" role="img" aria-label="Navy cover with a gold school building illustration"></div><p class="cover__title">CONDITIONED</p><p class="cover__author">Vikram Sethi</p></div>
      </div>
      <div class="winner col-b row-2 band-steel">
        <div class="winner__label"><span>LEADERSHIP &amp; MANAGEMENT</span></div>
        <div class="winner__photo photo-dark" role="img" aria-label="Portrait of author Owen Carlisle"></div>
        <div class="cover cover-cyan"><div class="cover__art" role="img" aria-label="Bright cyan cover"></div><p class="cover__title">PIVOT<br>THINKING</p><p class="cover__author">Owen Carlisle</p></div>
      </div>
      <div class="winner col-a row-3 band-navy">
        <div class="winner__label"><span>EDUCATION</span></div>
        <div class="winner__photo photo-studio" role="img" aria-label="Portrait of author Talia Renner"></div>
        <div class="cover cover-charcoal"><div class="cover__art" role="img" aria-label="Dark cover with the author seated on a gold block"></div><p class="cover__serif">RISING<br>HAND</p><p class="cover__author">Talia Renner</p></div>
      </div>
      <div class="winner col-b row-3 band-crimson">
        <div class="winner__label winner__label--long"><span>SALES &amp; BUSINESS PERFORMANCE</span></div>
        <div class="winner__photo photo-studio" role="img" aria-label="Portrait of author Greta Linden"></div>
        <div class="cover cover-sand"><div class="cover__art" role="img" aria-label="Cover with the author in a shop"></div><p class="cover__serif">The Year I Ran<br>a Bakery</p><p class="cover__author">Greta Linden</p></div>
      </div>

      <div class="sponsor"><span class="sponsor__dot"></span>TRS Press</div>
      <div class="footer">
        <svg viewBox="0 0 401 36" preserveAspectRatio="none"><path d="M0 26 C90 22 150 4 230 8 C310 12 360 22 401 16 L401 36 L0 36Z" fill="var(--frame)"/></svg>
        <p class="footer__url">pagefairnest.com.au</p>
      </div>
    </div>
  </section>

  <section class="poster poster--gold">
    <div class="poster__inner">
      <h1 class="title"><span class="title__book">BOOK</span><span class="title__year">OF THE YEAR</span><span class="title__num">2022</span></h1>
      <div class="event"><span class="event__mark">WPPF</span><span class="event__name">WRITERS PAGE PREMIERE AND FAIR</span></div>

      <div class="winner col-a row-1 band-gold">
        <div class="winner__label"><span>BOOK OF THE YEAR - GOLD</span></div>
        <div class="winner__photo photo-warm" role="img" aria-label="Portrait of author Maren Holloway"></div>
        <div class="cover cover-taupe"><div class="cover__art" role="img" aria-label="Cover artwork with the author seated"></div><p class="cover__author">Maren Holloway</p><p class="cover__title">TRADE</p></div>
      </div>
      <div class="winner col-b row-1 band-crimson">
        <div class="winner__label"><span>BOOK OF THE YEAR - SILVER</span></div>
        <div class="winner__photo photo-dark" role="img" aria-label="Portrait of author Delia Brennan"></div>
        <div class="cover cover-orange"><div class="cover__art" role="img" aria-label="Orange cover with a line drawing of open hands"></div><p class="cover__serif">the<em>Mindful</em>Steward</p><p class="cover__author">Delia Brennan</p></div>
      </div>
      <div class="winner col-a row-2 band-teal">
        <div class="winner__label"><span>BOOK OF THE YEAR - BRONZE</span></div>
        <div class="winner__photo photo-window" role="img" aria-label="Portrait of author Vikram Sethi"></div>
        <div class="cover cover-navy"><div class="cover__art" role="img" aria-label="Navy cover with a gold school building illustration"></div><p class="cover__title">CONDITIONED</p><p class="cover__author">Vikram Sethi</p></div>
      </div>
      <div class="winner col-b row-2 band-steel">
        <div class="winner__label"><span>LEADERSHIP &amp; MANAGEMENT</span></div>
        <div class="winner__photo photo-dark" role="img" aria-label="Portrait of author Owen Carlisle"></div>
        <div class="cover cover-cyan"><div class="cover__art" role="img" aria-label="Bright cyan cover"></div><p class="cover__title">PIVOT<br>THINKING</p><p class="cover__author">Owen Carlisle</p></div>
      </div>
      <div class="winner col-a row-3 band-navy">
        <div class="winner__label"><span>EDUCATION</span></div>
        <div class="winner__photo photo-studio" role="img" aria-label="Portrait of author Talia Renner"></div>
        <div class="cover cover-charcoal"><div class="cover__art" role="img" aria-label="Dark cover with the author seated on a gold block"></div><p class="cover__serif">RISING<br>HAND</p><p class="cover__author">Talia Renner</p></div>
      </div>
      <div class="winner col-b row-3 band-crimson">
        <div class="winner__label winner__label--long"><span>SALES &amp; BUSINESS PERFORMANCE</span></div>
        <div class="winner__photo photo-studio" role="img" aria-label="Portrait of author Greta Linden"></div>
        <div class="cover cover-sand"><div class="cover__art" role="img" aria-label="Cover with the author in a shop"></div><p class="cover__serif">The Year I Ran<br>a Bakery</p><p class="cover__author">Greta Linden</p></div>
      </div>

      <div class="sponsor"><span class="sponsor__dot"></span>TRS Press</div>
      <div class="footer">
        <svg viewBox="0 0 401 36" preserveAspectRatio="none"><path d="M0 26 C90 22 150 4 230 8 C310 12 360 22 401 16 L401 36 L0 36Z" fill="var(--frame)"/></svg>
        <p class="footer__url">pagefairnest.com.au</p>
      </div>
    </div>
  </section>

</div>
</body>
</html>
```